The Corbel Ridge Group's website for high impact furniture promotions

I am looking for a simple website. we are a promotional company that runs events for furniture stores to increase sales for short periods of time. i would like the website to have about 4 areas to explain our company. I would like it to be simple and user friendly. I would like a link to chatterbook and a contact section. I am attaching our logo that i would like somewhere large or possibly in the backround. I am open to different color schemes. I would like to convey fast paced, modern, reliable. I am open to all different styles and look forward to seeing whats out there. we are looking for a quick turn around, so if we see one that we like quick, we will pick that one thanks
Reason: looking for some really creative designs and want to give a fair amount of time to produce
Target Market(s)
Retail Furniture store owners
Industry/Entity Type
It Company
Number of Pages Required
1 page
Colors
Look and feel

```html
<!DOCTYPE html>
<html lang="en">
<head>
<meta charset="utf-8">
<title>The Corbel Ridge Group</title>
<link href="https://fonts.googleapis.com/css2?family=Open+Sans:wght@400;600;700&family=Crimson+Text:wght@400;700&display=swap" rel="stylesheet">
<style>
:root{
  --tan:#a6764c;
  --tan-light:#b88a60;
  --brown:#6b3f1e;
  --brown-dark:#4e2c12;
  --heading:#5a3417;
  --ink:#222;
  --muted:#a59a92;
  --grey-bg:#f1f0ef;
  --white:#fff;
}
*{margin:0;padding:0;box-sizing:border-box}
html,body{width:1200px;height:3586px;overflow:hidden}
body{font-family:"Open Sans",Arial,sans-serif;color:var(--ink);background:var(--white);position:relative}
.abs{position:absolute}
a{color:inherit;text-decoration:none}
svg{display:inline-block;vertical-align:middle}

/* top bar */
.topbar{left:0;top:0;width:1200px;height:38px;background:var(--tan);color:var(--white);font-size:17px}
.topbar .phone{left:44px;top:8px}
.topbar .account{right:34px;top:8px;display:flex;gap:26px}

/* nav */
.nav{left:0;top:38px;width:1200px;height:101px;background:var(--white)}
.brand{left:66px;top:18px;display:flex;flex-direction:column;align-items:center;gap:4px;color:var(--tan)}
.brand .dot{width:38px;height:38px;border-radius:50%;background:var(--tan)}
.brand .name{font-size:13px;font-weight:600;letter-spacing:1px;text-transform:uppercase}
.menu{right:38px;top:36px;display:flex;gap:36px;font-size:18px;color:var(--ink);font-weight:600}

/* hero */
.hero{left:0;top:139px;width:1200px;height:521px;background:linear-gradient(180deg,#e9e6e2 0%,#d8d2cb 45%,#b9aea3 100%)}
.hero .arrow{top:190px;width:52px;height:88px;background:rgba(166,118,76,.75);display:flex;align-items:center;justify-content:center}
.hero .arrow.l{left:40px}.hero .arrow.r{right:36px}
.hero-box{left:287px;top:148px;width:633px;height:263px;border:12px solid var(--white);background:rgba(120,95,75,.55);text-align:center;color:var(--white)}
.hero-box h1{font-family:"Crimson Text",Georgia,serif;font-size:44px;line-height:50px;font-weight:700;margin-top:38px;letter-spacing:1px}
.hero-box h1 span{font-weight:400}
.hero-box .rule{width:460px;height:3px;background:var(--white);margin:-26px auto 0}
.hero-box .btn{display:inline-block;margin-top:52px;background:var(--tan);border:2px solid #d9b894;padding:13px 28px;font-size:18px;text-transform:uppercase}
.dots{left:0;top:495px;width:1200px;display:flex;justify-content:center;gap:200px}
.dots i{width:6px;height:6px;border-radius:50%;background:rgba(255,255,255,.8)}

/* welcome */
.welcome h2{left:41px;top:708px;font-size:30px;font-weight:700;color:var(--heading)}
.welcome p{left:41px;top:756px;width:490px;font-size:18px;line-height:27px;color:var(--muted)}
.btn-tan{background:var(--tan);color:var(--white);font-size:18px;text-transform:uppercase;text-align:center}
.welcome .btn-tan{left:41px;top:944px;width:200px;height:55px;line-height:55px}
.sofa{left:598px;top:729px;width:562px;height:263px;background:radial-gradient(ellipse at 50% 55%,#b8683a 0%,#a05a30 45%,rgba(255,255,255,0) 70%)}

/* products */
.products{left:0;top:1071px;width:1200px;height:554px;background:linear-gradient(180deg,#b48760 0%,#9c6e47 55%,#a77a52 100%)}
.section-title{display:flex;align-items:center;justify-content:center;gap:16px;font-size:36px;font-weight:700}
.section-title .line{width:228px;height:3px}
.products .section-title{left:0;top:30px;width:1200px;color:var(--white)}
.products .section-title .line{background:var(--white)}
.products .sub{left:0;top:86px;width:1200px;text-align:center;color:var(--white);font-size:18px}
.card{top:148px;width:239px;height:318px;background:var(--brown-dark)}
.card .photo{width:239px;height:225px}
.card h3{color:var(--white);font-size:18px;font-weight:600;margin:9px 0 0 14px}
.card p{color:#eadbcc;font-size:15px;line-height:18px;margin:3px 0 0 14px;width:190px}
.card .go{right:12px;bottom:14px;width:14px;height:14px;border-radius:50%;background:var(--white)}

/* services */
.svc-photo{left:41px;top:1685px;width:576px;height:473px;background:linear-gradient(135deg,#5a3522 0%,#7a4a2f 45%,#d7c2a1 75%,#8e5a3a 100%)}
.svc-box{left:562px;top:1726px;width:602px;height:389px;background:var(--tan);color:var(--white)}
.svc-box h2{left:30px;top:22px;font-size:28px;font-weight:600}
.svc-box ul{left:30px;top:72px;list-style:none;width:540px}
.svc-box li{display:flex;gap:10px;font-size:20px;line-height:22px;margin-bottom:11px}
.svc-box .btn{left:56px;top:307px;width:206px;height:56px;line-height:56px;background:var(--white);color:var(--ink);text-align:center;font-size:18px;text-transform:uppercase}

/* gallery */
.gallery{left:0;top:2223px;width:1200px;height:437px;background:var(--grey-bg)}
.gallery .section-title{left:0;top:36px;width:1200px;color:var(--ink)}
.dark-line .line{background:var(--heading)}
.tile{top:126px;height:251px;background:var(--white)}
.tile.feature{background:linear-gradient(115deg,#7a4a2a 0%,#7a4a2a 55%,#e2dcd6 55%,#cdb8a9 100%);color:var(--white)}
.tile.feature h4{margin:22px 0 0 10px;font-size:18px;font-weight:600}
.tile.feature p{margin:12px 0 0 10px;font-size:14px;line-height:20px;width:150px}
.tile.feature .go{left:10px;top:146px;width:54px;height:54px;border-radius:50%;background:rgba(255,255,255,.35);display:flex;align-items:center;justify-content:center}
.tile .chair{left:50%;top:50%;transform:translate(-50%,-50%);width:160px;height:200px}

/* blog */
.blog .section-title{left:0;top:2700px;width:1200px;color:var(--ink)}
.post{top:2796px;width:353px}
.post .photo{height:282px;position:relative}
.post .date{position:absolute;left:38px;top:0;width:90px;height:108px;background:var(--brown);color:var(--white);text-align:center;padding-top:4px}
.post .date b{display:block;font-size:40px;font-weight:700;line-height:48px}
.post .date span{font-size:18px;letter-spacing:3px;text-transform:uppercase}
.post h3{font-size:23px;font-weight:700;margin-top:20px}
.post p{font-size:16px;line-height:20px;color:var(--muted);margin-top:6px}

/* footer */
.footer{left:0;top:3243px;width:1200px;height:343px;background:var(--brown);color:var(--white)}
.foot-brand{left:41px;top:36px;width:118px;height:86px;background:var(--white);display:flex;flex-direction:column;align-items:center;justify-content:center;gap:4px;color:var(--tan)}
.foot-brand .dot{width:30px;height:30px;border-radius:50%;background:var(--tan)}
.foot-brand .name{font-size:11px;font-weight:600;text-transform:uppercase;letter-spacing:.5px}
.footer .about{left:41px;top:132px;width:330px;font-size:15px;line-height:20px}
.footer .socials{left:41px;top:282px;display:flex;gap:10px}
.footer .socials i{width:38px;height:38px;border-radius:50%;background:rgba(255,255,255,.3)}
.footer h4{font-size:21px;font-weight:600;text-transform:uppercase;margin-bottom:12px;letter-spacing:.5px}
.footer ul{list-style:none;font-size:17px;line-height:24px}
.col1{left:445px;top:40px}.col2{left:662px;top:40px}.col3{left:892px;top:40px}
.contact-row{display:flex;gap:14px;font-size:18px;margin-bottom:14px;align-items:flex-start}
.contact-row.addr{font-size:16px;line-height:19px}
.footer .copy{right:38px;top:307px;font-size:16px}
</style>
</head>
<body>

<div class="topbar abs">
  <span class="phone abs"><svg width="14" height="14" viewBox="0 0 24 24"><path fill="#fff" d="M6.6 10.8a15 15 0 006.6 6.6l2.2-2.2c.3-.3.7-.4 1-.2 1.1.4 2.3.6 3.6.6.6 0 1 .4 1 1V20c0 .6-.4 1-1 1A17 17 0 013 4c0-.6.4-1 1-1h3.5c.6 0 1 .4 1 1 0 1.3.2 2.5.6 3.6.1.3 0 .7-.2 1z"/></svg> +252 -555- 0147</span>
  <div class="account abs">
    <a href="#">&#10140; Sign In</a>
    <a href="#"><svg width="13" height="14" viewBox="0 0 24 24"><circle cx="12" cy="7" r="5" fill="#fff"/><path fill="#fff" d="M2 23c0-6 4.5-9 10-9s10 3 10 9z"/></svg> Create an Account</a>
  </div>
</div>

<header class="nav abs">
  <div class="brand abs"><span class="dot"></span><span class="name">Corbel Ridge</span></div>
  <nav class="menu abs">
    <a href="#">HOME</a><a href="#">ABOUT US</a><a href="#">OUR STORE</a><a href="#">SERVICES</a><a href="#">GALLERY</a><a href="#">BLOG</a><a href="#">CONTACT US</a>
  </nav>
</header>

<section class="hero abs" role="img" aria-label="Bright living room with white sofas, lamps and framed pictures">
  <a class="arrow l abs" href="#"><svg width="18" height="26" viewBox="0 0 18 26"><path d="M14 3L4 13l10 10" stroke="#fff" stroke-width="4" fill="none"/></svg></a>
  <a class="arrow r abs" href="#"><svg width="18" height="26" viewBox="0 0 18 26"><path d="M4 3l10 10L4 23" stroke="#fff" stroke-width="4" fill="none"/></svg></a>
  <div class="hero-box abs">
    <h1>LOREN IPSUM DOLAR<br><span>SIT</span> AMET</h1>
    <div class="rule"></div>
    <a class="btn" href="#">Read More</a>
  </div>
  <div class="dots abs"><i></i><i></i><i></i><i></i><i></i></div>
</section>

<section class="welcome">
  <h2 class="abs">WELCOME TO OUR WEBSITE !</h2>
  <p class="abs">Donec eu efficitur urna, aliquam interdum felis. In hac habitasse platea dictumst. Nunc maximus facilisis ligula, eget ultricies sem bibendum eu.Donec eu efficitur urna, aliquam interdum felis. In hac habitasse platea dictumst. Nunc maximus facilisis ligula, eget ultricies sem bibendum eu.</p>
  <a class="btn-tan abs" href="#">Read More</a>
  <div class="sofa abs" role="img" aria-label="Tan leather three-seat sofa"></div>
</section>

<section class="products abs">
  <h2 class="section-title abs"><span class="line"></span>OUR PRODUCTS<span class="line"></span></h2>
  <p class="sub abs">Etiam consectetur fermentum condimentum. Donec sed tellus sed elit ornare consequat loren ipsum dolar sit</p>
  <div class="card abs" style="left:41px">
    <div class="photo" role="img" aria-label="Living room with navy sofa and patterned screen" style="background:linear-gradient(135deg,#c98e5c,#3b3f7a 60%,#e8e4e0)"></div>
    <h3>Loren Ipsum Dolar</h3><p>Quisque vitae fringilla leo, et tempus nulla.</p><span class="go abs"></span>
  </div>
  <div class="card abs" style="left:330px">
    <div class="photo" role="img" aria-label="White sectional sofa against dark wall" style="background:linear-gradient(180deg,#3b3b3d 0%,#55524f 50%,#eeeeec 75%,#cfcac5)"></div>
    <h3>Dolar Sit Amet</h3><p>Quisque vitae fringilla leo, et tempus nulla.</p><span class="go abs"></span>
  </div>
  <div class="card abs" style="left:626px">
    <div class="photo" role="img" aria-label="Cream sectional with red cushions by a fireplace" style="background:linear-gradient(160deg,#4a3a32 0%,#8a6a52 40%,#b8332a 65%,#e7dccd)"></div>
    <h3>Consiclet Ipsum Loren</h3><p>Quisque vitae fringilla leo, et tempus nulla.</p><span class="go abs"></span>
  </div>
  <div class="card abs" style="left:925px">
    <div class="photo" role="img" aria-label="Beige sofa in a room with mountain view windows" style="background:linear-gradient(170deg,#6b5a4a 0%,#a89585 40%,#e5d8c6 70%,#b89c80)"></div>
    <h3>Amet loren Ipsum</h3><p>Quisque vitae fringilla leo, et tempus nulla.</p><span class="go abs"></span>
  </div>
</section>

<section class="services">
  <div class="svc-photo abs" role="img" aria-label="Curved cream and brown modular sofa in a lounge"></div>
  <div class="svc-box abs">
    <h2 class="abs">OUR SERVICES &amp; MAINTENANCE</h2>
    <ul class="abs">
      <li><svg width="22" height="22" viewBox="0 0 22 22"><rect x="2" y="4" width="15" height="15" fill="none" stroke="#fff" stroke-width="2"/><path d="M6 11l4 4 10-11" stroke="#fff" stroke-width="2.5" fill="none"/></svg><span>Donec in placerat nibh. Duis convallis in risus sit amet dignissim loren ipsum</span></li>
      <li><svg width="22" height="22" viewBox="0 0 22 22"><rect x="2" y="4" width="15" height="15" fill="none" stroke="#fff" stroke-width="2"/><path d="M6 11l4 4 10-11" stroke="#fff" stroke-width="2.5" fill="none"/></svg><span>Donec in placerat nibh. Duis convallis in risus sit amet dignissim dolar</span></li>
      <li><svg width="22" height="22" viewBox="0 0 22 22"><rect x="2" y="4" width="15" height="15" fill="none" stroke="#fff" stroke-width="2"/><path d="M6 11l4 4 10-11" stroke="#fff" stroke-width="2.5" fill="none"/></svg><span>Donec in placerat nibh. Duis convallis in risus sit amet dignissim</span></li>
      <li><svg width="22" height="22" viewBox="0 0 22 22"><rect x="2" y="4" width="15" height="15" fill="none" stroke="#fff" stroke-width="2"/><path d="M6 11l4 4 10-11" stroke="#fff" stroke-width="2.5" fill="none"/></svg><span>Donec in placerat nibh. Duis convallis in risus sit amet dignissim</span></li>
    </ul>
    <a class="btn abs" href="#">Read More</a>
  </div>
</section>

<section class="gallery abs">
  <h2 class="section-title dark-line abs"><span class="line"></span>OUR GALLERY<span class="line"></span></h2>
  <div class="tile feature abs" style="left:41px;width:272px" role="img" aria-label="Red swivel chair">
    <h4>Loren Ipsum Dolar</h4>
    <p>Morbi quam risus, lobortis a dignissim ut,Morbi quam</p>
    <span class="go abs"><svg width="14" height="18" viewBox="0 0 14 18"><path d="M3 2l8 7-8 7" stroke="#fff" stroke-width="3" fill="none"/></svg></span>
  </div>
  <div class="tile abs" style="left:325px;width:270px"><div class="chair abs" role="img" aria-label="Cream armchair on chrome legs" style="background:radial-gradient(ellipse at 50% 40%,#e3ddd4 0%,#d3cbc0 50%,rgba(255,255,255,0) 72%)"></div></div>
  <div class="tile abs" style="left:607px;width:270px"><div class="chair abs" role="img" aria-label="Tufted white dining chair" style="background:radial-gradient(ellipse at 50% 40%,#f0ebe4 0%,#e0d8cc 50%,rgba(255,255,255,0) 72%)"></div></div>
  <div class="tile abs" style="left:889px;width:273px"><div class="chair abs" role="img" aria-label="Yellow and black designer loveseat" style="width:240px;background:radial-gradient(ellipse at 50% 45%,#f5c400 0%,#e8b400 40%,#2a2a2a 58%,rgba(255,255,255,0) 72%)"></div></div>
</section>

<section class="blog">
  <h2 class="section-title dark-line abs"><span class="line" style="width:280px"></span>OUR BLOG<span class="line" style="width:280px"></span></h2>
  <article class="post abs" style="left:41px">
    <div class="photo" role="img" aria-label="Living room with white sofas and red rug" style="background:linear-gradient(170deg,#8a6a4e 0%,#c9b9a6 45%,#f2eee9 65%,#9b2a1e)"><div class="date"><b>10</b><span>May</span></div></div>
    <h3>Loren Ipsum Dolar</h3>
    <p>Donec et purus at justo suscipit auctor id dictum risus. Sed eleifend lorem sit amet nisi aliquet, malesuada venenatis mi aliquet.</p>
  </article>
  <article class="post abs" style="left:421px">
    <div class="photo" role="img" aria-label="Black and white modern lounge with fireplace" style="background:linear-gradient(160deg,#e8e8e6 0%,#777 45%,#222 65%,#bbb)"><div class="date"><b>22</b><span>June</span></div></div>
    <h3>Dolar Sit Amet</h3>
    <p>Donec et purus at justo suscipit auctor id dictum risus. Sed eleifend lorem sit amet nisi aliquet, malesuada venenatis mi aliquet.</p>
  </article>
  <article class="post abs" style="left:808px">
    <div class="photo" role="img" aria-label="Sunny room with red sofa and television" style="background:linear-gradient(150deg,#6a8a40 0%,#d9c9a8 40%,#c0502a 70%,#e8ddd0)"><div class="date"><b>32</b><span>July</span></div></div>
    <h3>Consiclet Loren Ipsum</h3>
    <p>Donec et purus at justo suscipit auctor id dictum risus. Sed eleifend lorem sit amet nisi aliquet, malesuada venenatis mi aliquet.</p>
  </article>
</section>

<footer class="footer abs">
  <div class="foot-brand abs"><span class="dot"></span><span class="name">Corbel Ridge</span></div>
  <p class="about abs">Vestibulum ante ipsum primis in faucibus orci luctus et ultrices posuere cubilia Curae; Vivamus eu lorem a diam pharetra tempus.Vestibulum ante ipsum primis in faucibus orci luctus et ultrices posuere cubilia Curae; Vivamus eu lorem a diam pharetra tempus.</p>
  <div class="socials abs"><a href="#" aria-label="chatterbook"><i style="display:block"></i></a><i></i><i></i><i></i></div>
  <div class="col1 abs">
    <h4>Special Links</h4>
    <ul><li>Home</li><li>About Us</li><li>Services</li><li>Work</li><li>Blog</li><li>Contact Us</li></ul>
  </div>
  <div class="col2 abs">
    <h4>Other Links</h4>
    <ul><li>Create an Account</li><li>Login</li><li>Sign Up</li><li>Privacy Policy</li><li>Terms &amp; Conditions</li><li>FAQs</li></ul>
  </div>
  <div class="col3 abs">
    <h4>Get in Touch With Us</h4>
    <div class="contact-row"><svg width="16" height="16" viewBox="0 0 24 24"><path fill="#fff" d="M6.6 10.8a15 15 0 006.6 6.6l2.2-2.2c.3-.3.7-.4 1-.2 1.1.4 2.3.6 3.6.6.6 0 1 .4 1 1V20c0 .6-.4 1-1 1A17 17 0 013 4c0-.6.4-1 1-1h3.5c.6 0 1 .4 1 1 0 1.3.2 2.5.6 3.6.1.3 0 .7-.2 1z"/></svg><span>+252 -555- 0147</span></div>
    <div class="contact-row addr"><svg width="14" height="18" viewBox="0 0 14 20"><path fill="#fff" d="M7 0a7 7 0 00-7 7c0 5 7 13 7 13s7-8 7-13a7 7 0 00-7-7zm0 9.5A2.5 2.5 0 117 4.5a2.5 2.5 0 010 5z"/></svg><span>The Corbel Ridge Group<br>418 Birchfield Ln Cary,<br>North Carolina 27511<br>United States</span></div>
  </div>
  <p class="copy abs">Copyright2017.All Right Reserved</p>
</footer>

</body>
</html>
```